KESTREL Communications Business Card- Belsa

Kestrel Integrated Communications is Corporate communications agency with more than 20 years of experience. We become part of the manegement team of our clients in other to improve their outcomes and grow the possitioning of their brand.
We are in Puerto Rico, latin caribbean island
Name: Maribelsa (Belsa) Ocampo
787-555-0148
bocampo@kestrelwing.example

Target Market(s)

finance and pharmaceutical companies

Industry/Entity Type

Business

Contact Information for Business Card

modern, edgy colorful and playfull like our logo

Requirements
Must have
• company logo
• name
• tel
• email

```html
<!DOCTYPE html>
<html lang="en">
<head>
<meta charset="utf-8">
<title>Kestrel Integrated Communications – Business Card</title>
<link rel="stylesheet" href="https://fonts.googleapis.com/css2?family=Open+Sans:wght@400;600;700&display=swap">
<style>
  :root {
    --stage: #e4e4e2;
    --paper: #ffffff;
    --brand-orange: #f05a22;
    --brand-brown: #3f2c17;
    --ink-light: #ffffff;
  }
  * { margin: 0; padding: 0; box-sizing: border-box; }
  html, body {
    width: 1200px;
    height: 900px;
    overflow: hidden;
    background: var(--stage);
    font-family: "Open Sans", Arial, sans-serif;
  }
  .canvas {
    width: 1200px;
    height: 900px;
    display: flex;
    flex-direction: column;
    align-items: center;
    justify-content: center;
    gap: 60px;
  }
  .card {
    position: relative;
    width: 630px;
    height: 360px;
    background: var(--paper);
    box-shadow: 0 6px 18px rgba(0,0,0,0.12);
    overflow: hidden;
  }
  .brand-lockup {
    position: absolute;
    display: flex;
    align-items: center;
    gap: 12px;
    color: var(--brand-brown);
    font-weight: 700;
    line-height: 1.1;
  }
  .brand-dot {
    width: 18px;
    height: 18px;
    border-radius: 50%;
    background: var(--brand-orange);
    flex: none;
  }
  .card-front .brand-lockup {
    left: 50%;
    top: 50%;
    transform: translate(-50%, -50%);
    font-size: 30px;
  }
  .card-back .shape { position: absolute; inset: 0; }
  .card-back .brand-lockup {
    left: 36px;
    top: 118px;
    font-size: 22px;
  }
  .contact {
    position: absolute;
    right: 40px;
    top: 110px;
    color: var(--ink-light);
    text-align: right;
  }
  .contact-name {
    font-size: 24px;
    font-weight: 600;
    margin-bottom: 22px;
    margin-right: 34px;
  }
  .contact-list { list-style: none; }
  .contact-list li {
    display: flex;
    justify-content: flex-end;
    align-items: center;
    gap: 12px;
    font-size: 17px;
    line-height: 26px;
  }
  .contact-list svg { width: 16px; height: 16px; flex: none; }
</style>
</head>
<body>
<main class="canvas">

  <section class="card card-front" aria-label="Card front">
    <div class="brand-lockup">
      <span class="brand-dot"></span>
      <span>KESTREL<br>Communications</span>
    </div>
  </section>

  <section class="card card-back" aria-label="Card back">
    <svg class="shape" viewBox="0 0 630 360" width="630" height="360" aria-hidden="true">
      <path d="M282 0 C320 90 288 262 92 360 L630 360 L630 0 Z" fill="var(--brand-brown)"/>
      <path d="M298 0 C334 88 304 264 116 360 L630 360 L630 0 Z" fill="var(--paper)"/>
      <path d="M303 0 C339 88 309 264 123 360 L630 360 L630 0 Z" fill="var(--brand-orange)"/>
    </svg>

    <div class="brand-lockup">
      <span class="brand-dot"></span>
      <span>KESTREL<br>Communications</span>
    </div>

    <div class="contact">
      <p class="contact-name">Maribelsa Ocampo</p>
      <ul class="contact-list">
        <li>787-555-0148
          <svg viewBox="0 0 16 16" aria-hidden="true"><path d="M4 1.5 L6.5 4.5 L5 6.2 C6 8.3 7.7 10 9.8 11 L11.5 9.5 L14.5 12 L13 14.5 C7 14.5 1.5 9 1.5 3 Z" fill="var(--ink-light)"/></svg>
        </li>
        <li>bocampo@kestrelwing.example
          <svg viewBox="0 0 16 16" aria-hidden="true"><rect x="1.5" y="3.5" width="13" height="9" fill="var(--ink-light)"/><path d="M1.5 3.5 L8 9 L14.5 3.5" fill="none" stroke="var(--brand-orange)" stroke-width="1.2"/></svg>
        </li>
        <li>www.kestrelwing.example
          <svg viewBox="0 0 16 16" aria-hidden="true"><circle cx="8" cy="8" r="6.5" fill="var(--ink-light)"/><path d="M1.5 8 H14.5 M8 1.5 C5 5 5 11 8 14.5 M8 1.5 C11 5 11 11 8 14.5" fill="none" stroke="var(--brand-orange)" stroke-width="1"/></svg>
        </li>
      </ul>
    </div>
  </section>

</main>
</body>
</html>
```